A Label for an ECO Friendly Spirit Company

Design a label which can be used for vodka and gin (London Dry Gin). It should be Square type Like the Shape File you see in the uploads. VORK means Local Eco friendly Authentic and Fair. We want a cool and slim label that calls for eco-friendly. We want to use it for our premium
Vodka and our London Dry Gin. Please use the logo and design it in Square Type.

40%vol, 700ml

Target Market(s)

spirits and events

Industry/Entity Type

SPIRITS

Colors
00AB8E
00BBA5
67D7C9
C6EFE9
E9F9F6
59FF00
82FF00
B8FF75
E3FFCB
F4FFEA

Requirements
Must have
• Logo from VORK, Squaee Shape

```html
<!DOCTYPE html>
<html lang="en">
<head>
<meta charset="utf-8">
<title>VORK Dry Gin Label</title>
<link href="https://fonts.googleapis.com/css2?family=Montserrat:wght@700&family=Playfair+Display:wght@400&family=Lobster&display=swap" rel="stylesheet">
<style>
  :root {
    --page-bg: #f4f4f4;
    --label-green: #2f6a32;
    --label-field: #efebf4;
    --accent-lime: #9acd4a;
    --band-text: #ffffff;
  }
  html, body {
    margin: 0;
    padding: 0;
    width: 1167px;
    height: 1200px;
    overflow: hidden;
    background: var(--page-bg);
  }
  .label {
    position: relative;
    width: 1167px;
    height: 1200px;
  }
  .label-shape {
    position: absolute;
    inset: 0;
    width: 1167px;
    height: 1200px;
  }
  .frame { fill: var(--label-green); }
  .field { fill: var(--label-field); }
  .name-band { fill: var(--label-green); }
  .ornament-outline { fill: none; stroke: var(--label-green); stroke-width: 4; }
  .ornament-core { fill: var(--label-green); }
  .brand-square { fill: var(--accent-lime); }

  .brand-name {
    position: absolute;
    left: 0;
    width: 1167px;
    top: 600px;
    margin: 0;
    text-align: center;
    font-family: "Montserrat", sans-serif;
    font-weight: 700;
    font-size: 160px;
    line-height: 180px;
    letter-spacing: 2px;
    color: var(--label-green);
  }
  .spirit-type {
    position: absolute;
    left: 0;
    width: 1167px;
    top: 834px;
    height: 63px;
    margin: 0;
    text-align: center;
    font-family: "Lobster", cursive;
    font-weight: 400;
    font-size: 54px;
    line-height: 63px;
    color: var(--band-text);
  }
  .spec {
    position: absolute;
    margin: 0;
    font-family: "Playfair Display", serif;
    font-size: 36px;
    line-height: 40px;
    color: var(--label-green);
    white-space: nowrap;
  }
  .spec-strength {
    left: 256px;
    top: 586px;
    transform: translate(-50%, -50%) rotate(-45deg);
  }
  .spec-volume {
    left: 898px;
    top: 586px;
    transform: translate(-50%, -50%) rotate(45deg);
  }
</style>
</head>
<body>
  <main class="label">
    <svg class="label-shape" viewBox="0 0 1167 1200" xmlns="http://www.w3.org/2000/svg">
      <defs>
        <clipPath id="field-clip">
          <polygon points="583.5,178 1005.5,600 583.5,1022 161.5,600"/>
        </clipPath>
      </defs>
      <polygon class="frame" points="583.5,150 1033.5,600 583.5,1050 133.5,600"/>
      <polygon class="field" points="583.5,178 1005.5,600 583.5,1022 161.5,600" role="img" aria-label="Soft lavender field with a fine wavy line pattern"/>
      <rect class="name-band" x="0" y="834" width="1167" height="63" clip-path="url(#field-clip)"/>

      <g class="ornament ornament-top">
        <polygon class="ornament-outline" points="583.5,223 605.5,245 583.5,267 561.5,245"/>
        <polygon class="ornament-core" points="583.5,235 593.5,245 583.5,255 573.5,245"/>
      </g>
      <g class="ornament ornament-bottom">
        <polygon class="ornament-outline" points="583.5,943 605.5,965 583.5,987 561.5,965"/>
        <polygon class="ornament-core" points="583.5,955 593.5,965 583.5,975 573.5,965"/>
      </g>

      <rect class="brand-square" x="518.5" y="400" width="130" height="130" rx="10"/>
    </svg>

    <p class="spec spec-strength">40%vol</p>
    <p class="spec spec-volume">700ml</p>
    <h1 class="brand-name">VORK</h1>
    <p class="spirit-type">Dry Gin</p>
  </main>
</body>
</html>
```